Flyer for home based dog grooming salon

I need a flyer design for my home based dog grooming business. This flyer will be used for letterbox drops and supplied to local businesses such as vets. I may also extend the design at a later date for business cards as well.
Key advantages I want highlighted are listed below. They are listed in order of importance so that if the flyer becomes too busy, the less important items can be left off:
- "one on one personalised service where the groomer listens to your needs"
- NO CAGING...pets groomed immediately
- the same groomer for your pet at each groom, making your pet more comfortable
- local business in Wattle Reach
- modern, air-conditioned salon
- VIP program offering discounts for regular clients
List of services to be included are listed below:
- tidy-ups
- full-body clipping
- strip-outs
- breed specific clips
- and more...
Phone number, website and email address all need to be indicated clearly so they stand out
0438 615 294 (use the spacing as shown)
www.mirrabeetrims.com.au
info@mirrabeetrims.com.au
I have no strong preferences for colours, however, as I am a male groomer, I don't want the flyer to be too feminine but also not too masculine as many of the prospective customers are female.
I have seen good examples of flyers with images of dogs being groomed on them and flyers with just images of dogs on them and I have no preference for either - it will depend on the overall look of the flyer. If you wish to include images of dogs being groomed, I have uploaded 38 images of dogs being groomed taken from my salon. I don't want images of anyone else grooming dogs on the flyer. As i cater to all size dogs, any images of dogs do not need to limited to small breeds.
The flyer size will be DL (99 x 210 mm) and can be single or double sided. If you plan on doing double sided, please ensure the list of services offered is shown on the front side.
As an example of several designs I have seen before, in 2012 there was a project for Tarrowin Pawcare. From designs submitted, I liked #1135917, #1137543, #1135911 and probably would have gone for #1140593. I did not like the winner.

```html
<!DOCTYPE html>
<html lang="en">
<head>
<meta charset="utf-8">
<title>Mirrabee Trims – dog grooming salon flyers</title>
<link href="https://fonts.googleapis.com/css2?family=PT+Sans:wght@400;700&family=PT+Sans+Narrow:wght@700&family=Patrick+Hand&display=swap" rel="stylesheet">
<style>
  :root{
    --plum:#6d2a57;
    --olive:#8c9a52;
    --olive-text:#7f8e45;
    --sage:#d6e0bb;
    --card:#ece9e4;
    --card-streak:#e3dfd8;
    --ink:#4a4340;
    --page:#f3f1ec;
    --photo-green:#5f6b45;
    --photo-dark:#3b3833;
    --photo-cream:#e2d8c8;
    --photo-light:#d9d4cc;
  }
  *{box-sizing:border-box;margin:0;padding:0}
  html,body{width:1200px;height:1097px;overflow:hidden;background:var(--page)}
  .canvas{position:relative;width:1200px;height:1097px}
  .flyer{
    position:absolute;width:1063px;height:500px;
    background:linear-gradient(170deg,var(--card) 0%,var(--card-streak) 45%,var(--card) 100%);
    box-shadow:0 4px 14px rgba(0,0,0,.18);
    overflow:hidden;
    font-family:"PT Sans",sans-serif;color:var(--ink);
  }
  .flyer--front{left:30px;top:24px}
  .flyer--back{left:100px;top:557px}
  .brand{position:absolute;font-family:"PT Sans",sans-serif;font-weight:700;font-size:64px;color:var(--plum);letter-spacing:-.5px;line-height:1}
  .tagline{position:absolute;font-family:"Patrick Hand",cursive;font-size:34px;color:var(--olive-text);letter-spacing:1.5px;line-height:1}
  .brand-mark{position:absolute;width:70px;height:70px;border:3px solid var(--plum);border-radius:50%;background:#fff}
  .promise{
    position:absolute;left:24px;top:150px;width:574px;height:63px;
    background:var(--olive);border:2px solid #fff;border-radius:8px;
    display:flex;align-items:center;color:#fff;font-family:"PT Sans Narrow",sans-serif;
  }
  .promise__lead{padding-left:8px;line-height:1}
  .promise__big{display:block;font-size:32px}
  .promise__small{display:block;font-size:19px;margin-top:2px}
  .promise__text{margin-left:22px;font-size:18.5px;margin-top:10px}
  .panel{position:absolute;background:var(--sage);border:3px solid #fff;border-radius:16px}
  .advantages{left:26px;top:221px;width:574px;height:204px;padding:12px 10px 0 10px}
  .advantages li{list-style:none;position:relative;padding-left:28px;font-size:22.5px;line-height:27px;margin-bottom:5px}
  .bullet::before{content:"";position:absolute;left:4px;top:9px;width:11px;height:11px;border-radius:50%;background:var(--ink)}
  .photo{position:absolute;overflow:hidden;border:4px solid #fff}
  .photo--main{left:686px;top:132px;width:300px;height:300px;border-radius:16px;background:linear-gradient(160deg,var(--photo-green) 0%,var(--photo-green) 40%,var(--photo-dark) 60%,var(--photo-light) 100%)}
  .photo--round{border-radius:50%;background:radial-gradient(circle at 55% 45%,#f4f1ec 0%,var(--photo-light) 55%,#b9b2a8 100%)}
  .photo--tan{background:radial-gradient(circle at 50% 40%,var(--photo-cream) 0%,#cdb99a 60%,#4a4540 100%)}
  .photo--grey{background:radial-gradient(circle at 50% 50%,#d8d4ce 0%,#9a958c 60%,#3e3b37 100%)}
  .photo--tall{left:791px;top:90px;width:272px;height:380px;border:none;border-radius:0;background:linear-gradient(180deg,#e7e4df 0%,#d8d5d0 55%,#8a7a68 80%,#3d3935 100%)}
  .contact-bar{
    position:absolute;left:21px;top:443px;width:1023px;height:40px;
    background:var(--olive);border:2px solid #fff;border-radius:8px;
    display:flex;align-items:center;color:#fff;font-family:"PT Sans Narrow",sans-serif;font-size:22px;
  }
  .contact{display:flex;align-items:center;gap:7px;position:absolute}
  .contact svg{width:22px;height:22px}
  .contact--email{left:16px}
  .contact--web{left:388px}
  .contact--phone{right:18px;font-size:28px;letter-spacing:.5px}
  .services-head{
    position:absolute;left:22px;top:130px;width:324px;height:41px;
    background:var(--olive);border:2px solid #fff;border-radius:6px;
    color:#fff;font-family:"PT Sans",sans-serif;font-weight:700;font-size:26px;letter-spacing:.8px;
    display:flex;align-items:center;justify-content:center;z-index:2;
  }
  .services{left:34px;top:113px;width:301px;height:313px;padding:82px 0 0 22px}
  .services li{list-style:none;position:relative;padding-left:44px;font-size:27px;line-height:41px}
  .services .bullet::before{left:6px;top:14px;width:13px;height:13px}
</style>
</head>
<body>
<div class="canvas">

  <section class="flyer flyer--front">
    <h1 class="brand" style="left:64px;top:40px">Mirrabee Trims</h1>
    <p class="tagline" style="left:372px;top:112px">dog grooming salon</p>
    <span class="brand-mark" style="left:716px;top:34px" aria-hidden="true"></span>

    <div class="promise">
      <div class="promise__lead">
        <span class="promise__big">ONE on ONE</span>
        <span class="promise__small">personalised service</span>
      </div>
      <span class="promise__text">WHERE THE GROOMER LISTENS TO YOUR NEEDS</span>
    </div>

    <ul class="panel advantages">
      <li class="bullet">NO CAGING...pets groomed immediately</li>
      <li class="bullet">The same groomer for your pet at each groom, making your pet more comfortable</li>
      <li class="bullet">local business in Wattle Reach</li>
      <li class="bullet">Modern, air-conditioned salon</li>
      <li class="bullet">VIP program offering discounts for regular clients</li>
    </ul>

    <div class="photo photo--main" role="img" aria-label="Photo of the groomer seated outdoors holding a small white fluffy dog"></div>
    <div class="photo photo--round" style="left:910px;top:300px;width:136px;height:136px" role="img" aria-label="Close-up photo of a small white dog's head being trimmed with scissors"></div>

    <div class="contact-bar">
      <span class="contact contact--email">
        <svg viewBox="0 0 24 24" fill="none" stroke="#fff" stroke-width="2"><rect x="2" y="6" width="20" height="13" rx="1"/><path d="M2 7l10 7 10-7"/></svg>
        info@mirrabeetrims.com.au
      </span>
      <span class="contact contact--web">
        <svg viewBox="0 0 24 24" fill="none" stroke="#fff" stroke-width="2"><circle cx="12" cy="12" r="9"/><path d="M3 12h18M12 3c3 3 3 15 0 18M12 3c-3 3-3 15 0 18"/></svg>
        www.mirrabeetrims.com.au
      </span>
      <span class="contact contact--phone">
        <svg viewBox="0 0 24 24" fill="#fff"><path d="M6.6 10.8a15 15 0 006.6 6.6l2.2-2.2a1 1 0 011-.25 11.4 11.4 0 003.6.57 1 1 0 011 1V20a1 1 0 01-1 1A17 17 0 013 4a1 1 0 011-1h3.5a1 1 0 011 1c0 1.25.2 2.45.57 3.6a1 1 0 01-.25 1z"/></svg>
        0438 615 294
      </span>
    </div>
  </section>

  <section class="flyer flyer--back">
    <h2 class="brand" style="left:63px;top:34px">Mirrabee Trims</h2>
    <p class="tagline" style="left:363px;top:102px">dog grooming salon</p>
    <span class="brand-mark" style="left:686px;top:34px" aria-hidden="true"></span>

    <div class="photo photo--tall" role="img" aria-label="Photo of the groomer clipping a large white standard poodle"></div>

    <div class="services-head">GROOMING SERVICES</div>
    <ul class="panel services">
      <li class="bullet">Tidy-ups</li>
      <li class="bullet">Full-body Clipping</li>
      <li class="bullet">Strip-outs</li>
      <li class="bullet">Breed Specific Clips</li>
      <li class="bullet">And More...</li>
    </ul>

    <div class="photo photo--round" style="left:345px;top:159px;width:132px;height:132px" role="img" aria-label="Close-up photo of a small white dog's head being trimmed"></div>
    <div class="photo photo--round photo--tan" style="left:472px;top:238px;width:176px;height:176px" role="img" aria-label="Close-up photo of hands trimming a cream dog's paw"></div>
    <div class="photo photo--round photo--grey" style="left:669px;top:298px;width:132px;height:132px" role="img" aria-label="Close-up photo of a dog's leg being clipped on the grooming table"></div>

    <div class="contact-bar">
      <span class="contact contact--email">
        <svg viewBox="0 0 24 24" fill="none" stroke="#fff" stroke-width="2"><rect x="2" y="6" width="20" height="13" rx="1"/><path d="M2 7l10 7 10-7"/></svg>
        info@mirrabeetrims.com.au
      </span>
      <span class="contact contact--web">
        <svg viewBox="0 0 24 24" fill="none" stroke="#fff" stroke-width="2"><circle cx="12" cy="12" r="9"/><path d="M3 12h18M12 3c3 3 3 15 0 18M12 3c-3 3-3 15 0 18"/></svg>
        www.mirrabeetrims.com.au
      </span>
      <span class="contact contact--phone">
        <svg viewBox="0 0 24 24" fill="#fff"><path d="M6.6 10.8a15 15 0 006.6 6.6l2.2-2.2a1 1 0 011-.25 11.4 11.4 0 003.6.57 1 1 0 011 1V20a1 1 0 01-1 1A17 17 0 013 4a1 1 0 011-1h3.5a1 1 0 011 1c0 1.25.2 2.45.57 3.6a1 1 0 01-.25 1z"/></svg>
        0438 615 294
      </span>
    </div>
  </section>

</div>
</body>
</html>
```